velto GmbH - Business Cards etc.
velto GmbH
Project: velto GmbH - Business Cards etc.
velto GmbH - Business Cards etc. - Retailers
Creative Brief
Professional
Konrad Wieslauer
CEO
Gisela Brandtner Str. 23 76139 Karlsruhe
k.wieslauer@veltohouse.com
www.veltohouse.com
The business card MUST have the following format: 85 x 55mm PLUS a 3mm addition on every side. This means the image size must be 91 x 61mm
Concepts
Business Cards/Letterhead/ Envelopes/Notepads/Tshirt/labels for tiny tall crate
Business cards and company letter head for Osaka Dine Court
konrad konrad
I don't have a logo unfortunately. I've started a logo design project but it was not successful. I really need biz cards now and want to find a logo later. The logo on the biz cards is not so important in this case.
I wonder why there are so few contributions to this project? What's missing? How can I help?

```html
<!DOCTYPE html>
<html lang="de">
<head>
<meta charset="utf-8">
<title>velto GmbH – Visitenkarte Konrad Wieslauer</title>
<link rel="stylesheet" href="https://fonts.googleapis.com/css2?family=Tinos&family=Roboto+Condensed:wght@400;700&display=swap">
<style>
  :root {
    --page: #ffffff;
    --card: #59595b;
    --accent: #f28122;
    --text: #ffffff;
  }
  html, body {
    margin: 0;
    padding: 0;
    width: 1200px;
    height: 871px;
    overflow: hidden;
    background: var(--page);
  }
  .business-card {
    position: absolute;
    left: 156px;
    top: 149px;
    width: 888px;
    height: 571px;
    background: var(--card);
    color: var(--text);
  }
  .corner-mark {
    position: absolute;
    right: 0;
    top: 0;
    width: 84px;
    height: 53px;
    background: var(--accent);
  }
  .holder-name {
    position: absolute;
    left: 36px;
    top: 60px;
    margin: 0;
    font-family: "Tinos", "Times New Roman", serif;
    font-weight: 400;
    font-size: 62px;
    line-height: 1;
    letter-spacing: 0.2px;
  }
  .holder-role {
    position: absolute;
    left: 38px;
    top: 126px;
    margin: 0;
    font-family: "Roboto Condensed", "Arial Narrow", sans-serif;
    font-size: 27px;
    line-height: 1;
  }
  .brand-block {
    position: absolute;
    left: 0;
    bottom: 0;
    width: 377px;
    height: 209px;
    background: var(--accent);
    display: flex;
    align-items: center;
    padding-left: 38px;
    box-sizing: border-box;
  }
  .brand-name {
    font-family: "Roboto Condensed", "Arial Narrow", sans-serif;
    font-weight: 700;
    font-size: 58px;
    line-height: 1;
    color: var(--text);
    margin-top: -20px;
  }
  .contact-details {
    position: absolute;
    left: 389px;
    top: 360px;
    margin: 0;
    font-family: "Roboto Condensed", "Arial Narrow", sans-serif;
    font-style: normal;
    font-size: 25px;
    line-height: 30px;
    white-space: nowrap;
  }
  .contact-details span {
    display: block;
  }
</style>
</head>
<body>
  <section class="business-card">
    <div class="corner-mark"></div>
    <h1 class="holder-name">Konrad Wieslauer</h1>
    <p class="holder-role">CEO</p>
    <div class="brand-block">
      <span class="brand-name">velto GmbH</span>
    </div>
    <address class="contact-details">
      <span>Gisela Brandtner Str. 23</span>
      <span>76139 KarlsruhePhone +49 (0) 721 555 0142</span>
      <span>Fax +49 (0) 721 555 0143</span>
      <span>Email: k.wieslauer@veltohouse.com</span>
      <span>www.veltohouse.com</span>
    </address>
  </section>
</body>
</html>
```